Port Delridge is a new play by R. J. Halvorsen. The name Port Delridge refers to the location of the 1966 Brightwater - Tarrow Valley American football game. The play follows Joan Pelletier, who is approaching 70, as she unwillingly participates in a date dinner with Dennis Ashford, navigates the morning after at his apartment, and leaves, 15 months later, to take his granddaughter to college following her marriage to Dennis and his death. The play explores the definition of family, sex and aging, true love, overwhelming loss, political fanaticism, sexual assault, college football and “days of the week” panties. During the play, Joan tells lies, solves a mystery, picks a fight, critiques flavored condoms, loses her true love and survives. She lives her mother’s adage that “Being a woman is messy.” The poster will need an easily editable area for the theater and show time.

```html
<!DOCTYPE html>
<html lang="en">
<head>
<meta charset="utf-8">
<title>Port Delridge — a play by R. J. Halvorsen</title>
<link rel="stylesheet" href="https://fonts.googleapis.com/css2?family=Oswald:wght@500;700&display=swap">
<style>
  :root {
    --paper: #ffffff;
    --navy: #1c3f8e;
    --royal: #1f55b3;
    --sky: #2f6fd6;
    --ink: #0b0b0d;
    --type-light: #ffffff;
  }
  html, body {
    margin: 0;
    padding: 0;
    width: 900px;
    height: 1200px;
    overflow: hidden;
    background: var(--paper);
  }
  .poster {
    display: block;
    width: 900px;
    height: 1200px;
    background: var(--paper);
    font-family: "Oswald", "Arial Narrow", sans-serif;
  }
  .band--navy { fill: var(--navy); }
  .band--royal { fill: var(--royal); }
  .band--sky { fill: var(--sky); }
  .figure-silhouette { fill: var(--ink); }
  .band-text {
    fill: var(--type-light);
    font-weight: 500;
    text-transform: uppercase;
    letter-spacing: 1px;
  }
  .show-info { font-size: 50px; }
  .play-title { font-size: 96px; font-weight: 700; letter-spacing: 2px; }
  .playwright { font-size: 44px; }
  .tagline {
    fill: var(--type-light);
    font-size: 46px;
    font-weight: 500;
    letter-spacing: 1px;
  }
</style>
</head>
<body>
<svg class="poster" viewBox="0 0 900 1200" xmlns="http://www.w3.org/2000/svg">

  <!-- figure area -->
  <rect class="figure-silhouette" x="320" y="70" width="230" height="1010" rx="100"
        role="img" aria-label="Black silhouette of a standing woman, one hand on her hip"/>

  <!-- editable show information -->
  <g class="show-info-block">
    <g transform="translate(0 230) rotate(12)">
      <rect class="band--navy" x="-60" y="-55" width="480" height="80"/>
      <text class="band-text show-info show-day" x="20" y="10">Today at</text>
    </g>
    <g transform="translate(0 350) rotate(12)">
      <rect class="band--navy" x="-60" y="-55" width="1100" height="80"/>
      <text class="band-text show-info show-venue" x="20" y="10">The Acting Theatre</text>
    </g>
    <g transform="translate(0 465) rotate(12)">
      <rect class="band--royal" x="-60" y="-55" width="420" height="80"/>
      <text class="band-text show-info show-time" x="20" y="10">7 PM - 8 PM</text>
    </g>
  </g>

  <!-- title -->
  <g class="title-block" transform="translate(0 760) rotate(-15)">
    <rect class="band--navy" x="-60" y="-100" width="1160" height="170"/>
    <rect class="band--sky" x="-60" y="80" width="1160" height="60"/>
    <text class="band-text play-title" x="120" y="-10" textLength="670" lengthAdjust="spacingAndGlyphs">Port Delridge</text>
    <text class="band-text playwright" x="580" y="52" textLength="280" lengthAdjust="spacingAndGlyphs">by R. J. Halvorsen</text>
  </g>

  <!-- tagline bar -->
  <rect class="band--navy" x="0" y="1104" width="900" height="74"/>
  <text class="tagline" x="450" y="1159" text-anchor="middle">“BEING A WOMAN IS MESSY”</text>
</svg>
</body>
</html>
```